Consulting company requires a logo and business card design

I require a logo/business card design for a new company based in Sexsmith Alberta called TallMeadow Field Advisory Ltd. I plan to provide the following services: Construction management/inspection for the oil and gas industry, as well as general consulting for Asset Management, fleet management, etc. Have attached a copy of resume for use as guide for

Target Market(s)

Businesses within the oil and gas production, construction and shipping industry

Industry/Entity Type

Oil And Gas

Contact Information for Business Card

Believe should highlight, services offered, safety, quality,

Logo Text

TallMeadow Field Advisory (TMFA) ?

Font styles to use
Script

Requirements
Must have
• Open to all options

```html
<!DOCTYPE html>
<html lang="en">
<head>
<meta charset="utf-8">
<title>TallMeadow Field Advisory Ltd. — Business Card</title>
<link rel="stylesheet" href="https://fonts.googleapis.com/css2?family=Tinos:wght@400;700&display=swap">
<style>
  :root {
    --page-bg: #ecebe8;
    --card-white: #f7f7f7;
    --card-grey: #e9e9ea;
    --brand-blue: #1f7fc4;
    --band-light: #2b96cf;
    --band-dark: #1c63b3;
    --rule-dark: #1d2b3a;
    --ink: #161616;
    --on-blue: #ffffff;
  }
  * { box-sizing: border-box; margin: 0; padding: 0; }
  html, body { width: 1200px; height: 780px; overflow: hidden; }
  body {
    background: var(--page-bg);
    font-family: "Tinos", "Times New Roman", serif;
    position: relative;
  }
  .card {
    position: absolute;
    top: 235px;
    width: 540px;
    height: 310px;
    border-radius: 3px;
    overflow: hidden;
    box-shadow: 0 6px 18px rgba(0,0,0,.18);
  }
  .card--front {
    left: 40px;
    background: linear-gradient(180deg, var(--card-white) 0%, var(--card-grey) 100%);
  }
  .card--back { left: 620px; }

  /* front */
  .brand {
    color: var(--brand-blue);
    font-weight: 400;
    text-align: center;
  }
  .card--front .brand {
    position: absolute;
    top: 38px; left: 0; right: 0;
    font-size: 30px;
    letter-spacing: .5px;
  }
  .competencies-title {
    position: absolute;
    top: 104px; left: 0; right: 0;
    text-align: center;
    color: var(--brand-blue);
    font-size: 19px;
    letter-spacing: .5px;
  }
  .competencies {
    position: absolute;
    top: 140px; left: 20px; right: 20px;
    text-align: center;
    color: var(--ink);
    font-size: 16px;
    line-height: 24px;
  }
  .front-rule {
    position: absolute;
    left: 0; right: 0; top: 262px;
    height: 2px;
    background: var(--rule-dark);
  }
  .front-band {
    position: absolute;
    left: 0; right: 0; top: 266px; bottom: 0;
    background: linear-gradient(90deg, var(--band-dark), var(--band-light) 50%, var(--band-dark));
  }

  /* back */
  .back-top {
    position: absolute;
    left: 0; right: 0; top: 0;
    height: 132px;
    background: linear-gradient(180deg, var(--card-white), var(--card-grey));
  }
  .card--back .brand {
    position: absolute;
    top: 50px; left: 0; right: 0;
    font-size: 26px;
  }
  .back-rule {
    position: absolute;
    left: 0; right: 0; top: 132px;
    height: 2px;
    background: var(--rule-dark);
  }
  .back-panel {
    position: absolute;
    left: 0; right: 0; top: 134px; bottom: 0;
    background: linear-gradient(160deg, var(--band-light), var(--band-dark));
    color: var(--on-blue);
    padding: 22px 40px 0 60px;
  }
  .person-name {
    font-size: 22px;
    letter-spacing: 1px;
    text-transform: uppercase;
    margin-bottom: 18px;
  }
  .contact { list-style: none; font-size: 15px; line-height: 22px; }
</style>
</head>
<body>
  <section class="card card--front" aria-label="Card front">
    <h1 class="brand">TallMeadow Field Advisory Ltd.</h1>
    <h2 class="competencies-title">CORE COMPETENCIES</h2>
    <p class="competencies">
      Asset management | Strategic Planning | Process Improvement<br>
      Budget Planning &amp; Cost Control | Client Relations | Quality Control<br>
      Fleet Management | Construction Quality Management
    </p>
    <div class="front-rule"></div>
    <div class="front-band"></div>
  </section>

  <section class="card card--back" aria-label="Card back">
    <div class="back-top">
      <p class="brand">TallMeadow Field Advisory Ltd.</p>
    </div>
    <div class="back-rule"></div>
    <div class="back-panel">
      <p class="person-name">Daniel Marsh</p>
      <ul class="contact">
        <li>RR#4 Brookvale Alberta,</li>
        <li>T0X 1A0</li>
        <li>(555)014-2276</li>
        <li>danielmarsh61@fieldmail.ca</li>
      </ul>
    </div>
  </section>
</body>
</html>
```